Word Template Designs for Offensive Security Professional Services Report

We need a Microsoft Word Template designed for our Offensive Security professional services reports which includes the following services:

RedTeaming
Network Penetration Testing
Web Application Penetration Testing
Wireless Penetration Testing
Social Engineering

The templates should include the following:
Cover Page design with our Logo included
Executive Summary Page design
Detailed Findings Page design
Design for Last Page

Lastly, I would also like a template I can use for all of my Statements of Work

Requirements
Must have
• Beautiful Eye Catching HD pictures that represent my Offensive Security projects
The design should flow well with our logo

```html
<!DOCTYPE html>
<html lang="en">
<head>
<meta charset="utf-8">
<title>Breachline Labs – Scope of Work Template Pages</title>
<link rel="stylesheet" href="https://fonts.googleapis.com/css2?family=Lato:wght@400;700&family=Roboto:wght@400;500;700&display=swap">
<style>
:root{
  --stage:#4a4949;
  --paper:#ffffff;
  --ink:#222;
  --muted:#444;
  --green:#5c9a3c;
  --green-dark:#1d4a1f;
  --green-deep:#12331a;
  --black:#0b0b0b;
  --row-shade:#e3e3e3;
}
*{box-sizing:border-box;margin:0;padding:0}
html,body{width:1200px;height:1200px;overflow:hidden;background:var(--stage)}
body{position:relative;font-family:"Lato",sans-serif;color:var(--ink)}
.page{position:absolute;background:var(--paper);overflow:hidden}
.page-number{position:absolute;left:0;bottom:10px;background:var(--black);color:#fff;font-size:5.5px;padding:5px 10px;font-family:"Lato",sans-serif}

/* brand lockup */
.brand{display:flex;flex-direction:column;align-items:center;gap:3px}
.brand-mark{width:30px;height:30px;border-radius:50%;background:#2b2b2b}
.brand-name{font-family:"Roboto",sans-serif;font-weight:700;color:var(--green);font-size:10px;letter-spacing:.1px}
.page-header{position:absolute;left:0;right:0;top:14px}
.header-rule{position:absolute;left:0;right:0;height:2px;background:var(--green)}

/* cover */
.cover{left:54px;top:95px;width:335px;height:474px;background:var(--green-dark)}
.cover-art{position:absolute;inset:0;background:
  radial-gradient(circle at 40% 70%, #3f7a33 0%, transparent 45%),
  radial-gradient(circle at 75% 25%, #2f6a2a 0%, transparent 50%),
  linear-gradient(160deg,#2a5a28 0%,#1a4220 55%,#10301a 100%)}
.cover .brand{position:absolute;top:18px;left:0;right:0}
.cover .brand-mark{width:48px;height:48px;background:#1a1a1a;border:2px solid #3a3a3a}
.cover .brand-name{font-size:17px}
.cover-title{position:absolute;left:61px;top:127px;color:#fff;font-family:"Roboto",sans-serif;font-weight:500;font-size:11px;line-height:13.5px}
.cover-client{position:absolute;left:61px;top:177px;color:#fff;font-family:"Roboto",sans-serif;font-weight:500;font-size:7.5px;line-height:9.5px}
.cover-prepared{position:absolute;left:188px;top:325px;border-left:2px solid #fff;padding-left:8px;color:#fff;font-family:"Roboto",sans-serif;font-weight:500;font-size:6.4px;line-height:8.3px}
.cover-prepared p+p{margin-top:7px}
.cover-footer{position:absolute;left:0;right:0;bottom:0;height:40px;background:var(--black);border-top:3px solid #fff;display:flex;justify-content:space-around;align-items:center;color:#fff;font-size:5.5px}
.cover-footer span{display:flex;align-items:center;gap:4px}
.cover-footer svg{width:7px;height:7px}

/* revision */
.revision{left:430px;top:97px;width:330px;height:466px}
.revision h2{position:absolute;top:21px;left:0;right:0;text-align:center;font-family:"Roboto",sans-serif;color:var(--green);font-size:13px;font-weight:700}
.revision-table{position:absolute;top:44px;left:0;right:0;border-collapse:collapse;width:100%}
.revision-table th{background:var(--black);color:#fff;font-family:"Roboto",sans-serif;font-weight:400;font-size:8.5px;text-align:left;padding:4px 0 4px 20px;height:18px}
.revision-table td{font-size:5px;padding:6px 0 0 22px}

/* toc */
.toc{left:804px;top:92px;width:334px;height:473px}
.toc .brand{position:absolute;top:15px;left:0;right:0}
.toc-band{position:absolute;top:77px;left:0;right:0;height:52px;background:var(--green);color:#fff;display:flex;align-items:center;justify-content:center;font-family:"Roboto",sans-serif;font-weight:700;font-size:16px}
.toc-list{position:absolute;top:136px;left:0;right:0;list-style:none}
.toc-list li{display:flex;justify-content:space-between;height:16.8px;align-items:center;padding:0 18px 0 13px;font-size:5.6px;color:#222}
.toc-list li.major{background:var(--row-shade);font-weight:700}
.toc-list li.upper{text-transform:uppercase}

/* content pages */
.content h3{font-family:"Roboto",sans-serif;font-weight:700;color:var(--green);font-size:9.6px;border-left:2.5px solid var(--black);padding-left:3px;line-height:10px;margin:8px 0 4px}
.content p{font-size:4.6px;line-height:5.6px;color:var(--muted);margin-bottom:4px}
.content .lead{color:var(--green)}
.content .body{position:absolute;left:8px;right:10px}
.ticks{display:grid;grid-template-columns:1fr 1fr;gap:3px 0;list-style:none;margin:3px 0 4px 6px}
.ticks li{font-size:4.6px;color:#333;display:flex;gap:3px;align-items:center}
.ticks li::before{content:"\2713";color:var(--green);font-size:5px}

.p4{left:58px;top:633px;width:334px;height:473px}
.p5{left:432px;top:630px;width:339px;height:480px}
.p6{left:804px;top:627px;width:338px;height:478px}

.test-panel{margin:8px 11px 6px 11px;height:127px;background:linear-gradient(135deg,#5c9a3c,#4c8a32);display:grid;grid-template-columns:1fr 1fr;padding:10px 20px 10px 24px;position:relative}
.test-panel::after{content:"";position:absolute;left:50%;top:6px;bottom:6px;width:1px;background:rgba(255,255,255,.6)}
.test-panel ul{list-style:none;display:flex;flex-direction:column;gap:6px}
.test-panel li{color:#fff;font-size:4.8px;display:flex;gap:3px}
.test-panel li::before{content:"\2713";font-size:5px}
.test-panel ul+ul{padding-left:14px;gap:5.4px}

.bullets{list-style:none;margin:6px 0 0 12px}
.bullets li{font-size:4.8px;color:#333;margin-bottom:8px;display:flex;gap:4px}
.bullets li::before{content:"";width:3px;height:3px;border-radius:50%;background:var(--green);margin-top:1px;flex:none}
</style>
</head>
<body>

<!-- Cover -->
<section class="page cover">
  <div class="cover-art" role="img" aria-label="Green-toned photograph of a hand reaching toward a digital padlock and network graphic"></div>
  <div class="brand">
    <div class="brand-mark"></div>
    <div class="brand-name">Breachline Labs</div>
  </div>
  <h1 class="cover-title">Scope of Work :<br>External, Internal Network, Wireless and Web<br>ApplicationPenetration Testing Engagement</h1>
  <p class="cover-client">PREPARED FOR :<br>[Client Name]</p>
  <div class="cover-prepared">
    <p>PREPARED BY :<br>Daniel Corvin, CISSP, OSCE, OSCP<br>[Company Name], LLC</p>
    <p>4210 Ridge Park Dr Suite 210<br>Austin Texas 78701<br>www.breachline-labs.com</p>
    <p>Daniel.Corvin@Breachline-Labs.com<br>Office 1800.555.0143<br>Mobile: 512.555.0188<br>August 2, 2018</p>
  </div>
  <footer class="cover-footer">
    <span><svg viewBox="0 0 10 10"><circle cx="5" cy="5" r="4.3" fill="none" stroke="#fff"/><path d="M3.5 3 l1 0 l.4 1.2 l-.6.5 a3 3 0 0 0 1.5 1.5 l.5-.6 l1.2.4 l0 1 a4 4 0 0 1-4-4z" fill="#fff"/></svg>1-800-555-0143</span>
    <span><svg viewBox="0 0 10 10"><rect x="1" y="2.5" width="8" height="5" fill="#fff"/><path d="M1 2.5 L5 5.5 L9 2.5" stroke="#000" stroke-width=".7" fill="none"/></svg>info@example.com</span>
    <span><svg viewBox="0 0 10 10"><circle cx="5" cy="5" r="4.3" fill="#fff"/><path d="M.7 5h8.6M5 .7v8.6" stroke="#000" stroke-width=".5"/></svg>www.breachline-labs.com</span>
  </footer>
</section>

<!-- Revision control -->
<section class="page revision">
  <h2>DOCUMENT REVISION CONTROL</h2>
  <table class="revision-table">
    <thead><tr><th style="width:38%">Revision Number</th><th style="width:44%">Revision</th><th>Revision Date</th></tr></thead>
    <tbody><tr><td>1.0</td><td>Initial</td><td>8/2/18</td></tr></tbody>
  </table>
  <div class="page-number">Page 2</div>
</section>

<!-- Table of contents -->
<section class="page toc">
  <div class="brand"><div class="brand-mark"></div><div class="brand-name">Breachline Labs</div></div>
  <div class="toc-band">TABLE OF CONTENTS</div>
  <ul class="toc-list">
    <li class="upper"><span>Table of Contents</span><span>3</span></li>
    <li class="major upper"><span>Proposal Summary</span><span>4</span></li>
    <li class="upper"><span>Engagement Overview</span><span>4</span></li>
    <li><span>Phase One: External Network Penetration Testing</span><span>4</span></li>
    <li><span>Phase Two: Internal Network Penetration Testing</span><span>4</span></li>
    <li><span>Phase Three: Wireless Penetration Testing</span><span>5</span></li>
    <li><span>Phase Four: Targeted Web Application Penetration Testing</span><span>5</span></li>
    <li class="upper"><span>Engagement Deliverables</span><span>6</span></li>
    <li class="upper"><span>Phase Specific Tasks</span><span>7</span></li>
    <li><span>Phase One: External Network Penetration Testing</span><span>7</span></li>
    <li><span>Phase Two: Internal Network Penetration Testing</span><span>9</span></li>
    <li><span>Phase Three: Wireless Penetration Testing</span><span>11</span></li>
    <li><span>Phase Four: Targeted Web Application Penetration Testing</span><span>12</span></li>
    <li class="major upper"><span>About [Company Name]</span><span>15</span></li>
    <li class="upper"><span>Consultant Profile</span><span>15</span></li>
    <li class="major upper"><span>Scope Approval</span><span>16</span></li>
    <li class="upper"><span>Client Activity Checklist</span><span>16</span></li>
    <li class="upper"><span>Acknowledgements</span><span>16</span></li>
  </ul>
  <div class="page-number">Page 3</div>
</section>

<!-- Page 4 -->
<section class="page content p4">
  <div class="page-header"><div class="brand"><div class="brand-mark"></div><div class="brand-name">Breachline Labs</div></div></div>
  <div class="header-rule" style="top:71px"></div>
  <div class="body" style="top:77px">
    <h3>PROPOSAL SUMMARY</h3>
    <p>[Company Name] is proud to present this multi-phase Scope of Work to [Client Name] to meet their Penetration Testing Requirements. [Company Name] LLC's security consultants have expert knowledge in Network Security and Web Applications, Security Controls, process and procedures, best practices, vulnerabilities and countermeasures. Our security consultants will perform the penetration testing presented in this Scope of Work.</p>
    <h3>ENGAGEMENT OVERVIEW</h3>
    <p>Based on the information provided, [Company Name] understands that [Client Name] objectives are to have [Company Name] LLC provide penetration testing, ethical hacking and risk management services to [Client Name] to help ensure that the systems are working in a safe secure manner in every respect and by ensuring the proper preservation of all data's Confidentiality, Integrity, and Availability (CIA).</p>
    <p>From [Company Name]'s understanding, [Client Name] has requested that the penetration testing be performed from a grey box perspective to determine the exposed vulnerabilities of the networks, applications and wireless implementations.</p>
    <p class="lead">In response to these requirements, [Company Name] will perform the following services :</p>
    <ul class="ticks">
      <li>External Network Penetration Testing</li><li>Internal Network Penetration Testing</li>
      <li>Wireless Network Penetration Testing</li><li>Targeted Web Application Penetration Testing</li>
    </ul>
    <h3>PHASE ONE: EXTERNAL NETWORK PENETRATION TESTING</h3>
    <p>[Company Name] will conduct a Network Penetration Testing assessment of the external network, aka the Internet presence to help identify existing vulnerabilities and their associated risks. [Company Name] will discover and identify hosts belonging to [Client Name] external network, identify vulnerabilities and exploit vulnerabilities identified during the ethical hacking process. After a system is compromised, the vulnerabilities and any applicable exploits will be documented in a detailed, repeatable process.</p>
    <p>[Company Name] will conduct this work remotely while performing the Network Penetration Testing assessment in collaboration with [Client Name] personnel. After the assessment is complete, [Company Name] will develop a formal report that will include the items described in the Final Report Summary.</p>
    <h3>PHASE TWO: INTERNAL NETWORK PENETRATION TESTING</h3>
    <p>[Company Name] will conduct a penetration test of the [Client Name] internal network, aka their private LAN. [Company Name] will exploit vulnerabilities identified during the vulnerability identification process. After a system is compromised, the vulnerabilities and any applicable exploits will be documented in a detailed, repeatable process.</p>
    <p>[Company Name] will conduct this work onsite initially and remotely after deploying [Company Name]'s internal network attack server. The Network Penetration Testing will be conducted in collaboration with [Client Name] personnel. After the assessment is complete, [Company Name] will develop a formal report that will include the items described in the Final Report Summary.</p>
    <p style="margin-top:6px"><b style="color:#222">Note :</b> The attack server's purpose is to facilitate internal network penetration testing efforts from a remote offsite location. This will help emulate an attacker who has gained access to the internal network and is outside of the organization. No Denial of Service or testing outside of the internal network penetration testing efforts will be conducted via the attack server.</p>
  </div>
  <div class="page-number">Page 4</div>
</section>

<!-- Page 5 -->
<section class="page content p5">
  <div class="page-header"><div class="brand"><div class="brand-mark"></div><div class="brand-name">Breachline Labs</div></div></div>
  <div class="header-rule" style="top:72px"></div>
  <div class="body" style="top:78px">
    <h3>PHASE THREE:WIRELESS PENETRATION TESTING</h3>
    <p>[Company Name] will assess [Client Name] guest and production wireless networks. During testing, [Company Name] will attempt to gain access to hosts belonging to [Client Name]' internal network presence and wireless controllers. [Company Name] will exploit vulnerabilities identified during the vulnerability identification process. After a system or information is compromised, [Company Name] will gather appropriate evidence for proof of information or system compromise.</p>
    <p>[Company Name] will conduct this work on-site while performing the assessment in collaboration with [Client Name]. After the assessment is complete, [Company Name] will develop a formal report that will include the items described in the Final Report Summary.</p>
    <h3>PHASE FOUR: TARGETED WEB APPLICATION<br>PENETRATION TESTING</h3>
    <p>[Company Name] will conduct a Targeted Web Application Penetration Testing assessment of the target web application and supporting services as an unauthorized/unauthenticated and authorized/authenticated users' perspective to determine the exposed vulnerabilities that are accessible to an attacker.</p>
    <p><span class="lead">Unauthorized/Unauthenticated</span> - An Unauthenticated Assessment of your web application gives a realistic view of what an attacker with a simple Internet connection and no privileges would be able to access, find, and possibly exploit. This type of assessment tests the strengths of your application's authentication mechanism(s) and any other vulnerability associated with the application.</p>
    <p><span class="lead">Authorized/Authenticated</span> - An authenticated Assessment of your web application gives a realistic view of what an attacker with basic and administrative privileges would be able to access, find, and possibly exploit. This type of assessment tests the strengths of your applications to withstand attacks by authorized users who have valid credentials to authenticate to the application.</p>
    <p>Additional testing may include the following :</p>
  </div>
  <div style="position:absolute;left:0;right:0;top:287px">
    <div class="test-panel" role="img" aria-label="Green panel over a faint technology photograph listing additional web application tests">
      <ul>
        <li>Information Leakage</li><li>Session Management</li><li>Default Configurations</li><li>Authentication abuse</li><li>Client-Side Cache</li><li>Authorization exploitation</li><li>SQL Injection, (backend database<br>enumeration and manipulation)</li>
      </ul>
      <ul>
        <li>OS Command Injection</li><li>Local and Remote File Inclusion</li><li>Cross Site Request Forgery</li><li>Application and Business Logic Flaws</li><li>Proper Input Validation</li><li>Privilege Escalation Opportunities</li><li>Client-Side Code</li><li>Server-Side Input Validation</li>
      </ul>
    </div>
    <p style="font-size:4.6px;line-height:5.6px;color:#444;margin:0 14px">[Company Name] follows a well-developed and proven methodology to assess the security of web-based applications as defined in the specific tasks in the next section. After the assessment is complete, [Company Name] will develop a formal report that will include the items described in the Final Report Summary.</p>
  </div>
  <div class="page-number">Page 5</div>
</section>

<!-- Page 6 -->
<section class="page content p6">
  <div class="page-header"><div class="brand"><div class="brand-mark"></div><div class="brand-name">Breachline Labs</div></div></div>
  <div class="header-rule" style="top:71px"></div>
  <div class="body" style="top:78px;left:12px">
    <h3>ENGAGEMENT DELIVERABLES</h3>
    <p style="margin-left:8px">[Company Name] will provide the following Deliverables to [Client Name]:</p>
    <ul class="bullets">
      <li>Weekly Status Updates if applicable</li>
      <li>Final Report and Presentation delivered at the end of the engagement</li>
      <li>Onsite Q&amp;A session with our consultants to discuss the process, findings, and recommendations, and answer<br>questions related to the engagement.</li>
    </ul>
  </div>
  <div class="page-number">Page 6</div>
</section>

</body>
</html>
```